Car finance company business card

Create a nice business card for our car financing company , Visit our website www.birchlanefinance.com for the phone number and idea of the company look. Please do not be afraid to be creative. Name on card Is Marc-Antoine Beaulieu and phone number is on our website adress of business is
27816 Boulevard Saint-Orvel,
Mirabel, QC K4R 2T8

```html
<!DOCTYPE html>
<html lang="en">
<head>
<meta charset="utf-8">
<title>Birch Lane Finance – Business Card</title>
<link href="https://fonts.googleapis.com/css2?family=Crimson+Text:wght@400;600&display=swap" rel="stylesheet">
<style>
  :root {
    --page-bg: #e9ecef;
    --card-top: #1d4a52;
    --card-mid: #0f3a2c;
    --card-bottom: #1f5a3a;
    --accent-orange: #e0692c;
    --text-soft: #e9c9a4;
    --text-light: #f1e3cf;
    --brand-silver: #dfe3e6;
    --icon-orange: #d8652a;
    --mascot-orange: #d86a2a;
    --mascot-dark: #3b3f3a;
  }
  * { margin: 0; padding: 0; box-sizing: border-box; }
  html, body {
    width: 1200px; height: 1200px; overflow: hidden;
    background: var(--page-bg);
  }
  .canvas {
    width: 1200px; height: 1200px;
    display: flex; align-items: center; justify-content: center;
  }
  .business-card {
    position: relative;
    width: 1100px; height: 628px;
    border-radius: 8px;
    overflow: hidden;
    background:
      radial-gradient(ellipse at 30% 60%, var(--card-mid) 0%, transparent 70%),
      linear-gradient(160deg, var(--card-top) 0%, var(--card-mid) 55%, var(--card-bottom) 100%);
    box-shadow: 0 20px 50px rgba(0,0,0,0.25);
    font-family: "Crimson Text", Georgia, serif;
  }
  .brand {
    position: absolute; left: 70px; top: 100px;
    width: 520px;
    display: flex; align-items: center; gap: 16px;
  }
  .brand-dot {
    width: 40px; height: 40px; border-radius: 50%; flex: none;
    background: var(--brand-silver);
  }
  .brand-name {
    font-family: "Crimson Text", Georgia, serif;
    font-weight: 600; font-size: 50px; line-height: 1;
    color: var(--brand-silver);
    white-space: nowrap;
  }
  .contact-block {
    position: absolute; left: 70px; top: 290px;
    width: 540px;
    color: var(--text-soft);
  }
  .person-name {
    font-size: 38px; font-weight: 400; color: var(--accent-orange);
    text-transform: uppercase; letter-spacing: 0.5px; line-height: 1.05;
    white-space: nowrap;
  }
  .person-role {
    font-size: 28px; color: var(--text-light); margin-bottom: 22px;
  }
  .address { font-size: 28px; line-height: 1.2; margin-bottom: 18px; }
  .contact-list { list-style: none; font-size: 28px; line-height: 1.25; }
  .contact-list li { display: flex; align-items: center; gap: 14px; }
  .contact-list svg { width: 20px; height: 20px; flex: none; }
  .mascot {
    position: absolute; right: 60px; top: 70px;
    width: 400px; height: 500px; border-radius: 40% 45% 30% 35%;
    background: radial-gradient(ellipse at 50% 40%, var(--mascot-orange) 0%, #a9521f 45%, var(--mascot-dark) 100%);
    opacity: 0.85;
  }
</style>
</head>
<body>
<main class="canvas">
  <article class="business-card">
    <header class="brand">
      <span class="brand-dot"></span>
      <span class="brand-name">Birch Lane Finance</span>
    </header>

    <section class="contact-block">
      <h1 class="person-name">Marc-Antoine Beaulieu</h1>
      <p class="person-role">manager</p>
      <p class="address">27816 Boulevard Saint-Orvel,<br>Mirabel, QC K4R 2T8</p>
      <ul class="contact-list">
        <li>
          <svg viewBox="0 0 24 24" aria-hidden="true"><path fill="var(--icon-orange)" d="M6.6 10.8a15.1 15.1 0 0 0 6.6 6.6l2.2-2.2c.3-.3.7-.4 1-.2 1.1.4 2.3.6 3.6.6.6 0 1 .4 1 1V20c0 .6-.4 1-1 1A17 17 0 0 1 3 4c0-.6.4-1 1-1h3.5c.6 0 1 .4 1 1 0 1.3.2 2.5.6 3.6.1.3 0 .7-.2 1z"/></svg>
          +(450) - 555 - 0182
        </li>
        <li>
          <svg viewBox="0 0 24 24" aria-hidden="true"><rect x="2" y="5" width="20" height="14" rx="1" fill="var(--icon-orange)"/><path d="M2 6l10 7 10-7" fill="none" stroke="#0f3a2c" stroke-width="1.6"/></svg>
          info@birchlanefinance.com
        </li>
        <li>
          <svg viewBox="0 0 24 24" aria-hidden="true"><circle cx="12" cy="12" r="9" fill="none" stroke="var(--icon-orange)" stroke-width="2"/><path d="M3 12h18M12 3c3 3 3 15 0 18M12 3c-3 3-3 15 0 18" fill="none" stroke="var(--icon-orange)" stroke-width="1.5"/></svg>
          www.birchlanefinance.com
        </li>
      </ul>
    </section>

    <div class="mascot" role="img" aria-label="Cartoon fox mascot in a suit giving a thumbs up and holding car keys"></div>
  </article>
</main>
</body>
</html>
```